Breezeway Climate Business Card Design

Design new, 2 sides, business cards for a residential and light commercial heating, air conditioning contractor.

Target Market(s)

Homeowners, small businesses

Industry/Entity Type

Business

Contact Information for Business Card

Dominic Vasquerelli
Phone - 555-214-6837
Email
Address - PO box 618
Millbrook NJ 07999
Website - www.BreezewayClimateLLC.example

Requirements
Must have
• logo, company colors, standard size with no die cut, so I can use printhaven

```html
<!DOCTYPE html>
<html lang="en">
<head>
<meta charset="utf-8">
<title>Breezeway Climate Business Card</title>
<link rel="stylesheet" href="https://fonts.googleapis.com/css2?family=Open+Sans:wght@400;600;700&display=swap">
<style>
  :root {
    --bg: #2b2b2d;
    --card-red: #a32033;
    --card-white: #ffffff;
    --gold: #f3d47c;
    --cream: #fbeec8;
    --text-light: #ffffff;
  }
  * { margin: 0; padding: 0; box-sizing: border-box; }
  html, body { width: 1200px; height: 1200px; overflow: hidden; }
  body {
    background: var(--bg);
    font-family: "Open Sans", Arial, sans-serif;
    position: relative;
  }
  .card {
    position: absolute;
    top: 240px;
    width: 400px;
    height: 700px;
    background: var(--card-red);
    overflow: hidden;
    box-shadow: 0 8px 24px rgba(0,0,0,0.35);
  }
  .card--front { left: 160px; }
  .card--back { left: 640px; }

  .front__header {
    position: absolute;
    top: 0; left: 0; right: 0;
    height: 210px;
    background: var(--card-white);
  }
  .brand-name {
    position: absolute;
    left: 0; right: 0;
    text-align: center;
    font-weight: 700;
    font-size: 40px;
    line-height: 1.1;
    letter-spacing: 0.5px;
  }
  .card--front .brand-name { top: 120px; color: var(--card-red); }
  .card--back .brand-name { top: 260px; color: var(--text-light); }

  .person {
    position: absolute;
    top: 430px; left: 0; right: 0;
    text-align: center;
  }
  .person__name {
    color: var(--gold);
    font-weight: 600;
    font-size: 20px;
  }
  .person__title {
    color: var(--cream);
    font-size: 15px;
    margin-top: 2px;
  }

  .contact {
    position: absolute;
    top: 545px; left: 0; right: 0;
    text-align: center;
    color: var(--text-light);
    font-size: 16px;
    line-height: 1.45;
  }
  .contact__icons {
    display: flex;
    justify-content: center;
    gap: 6px;
    margin-bottom: 6px;
  }
  .contact__icon { width: 22px; height: 22px; }
</style>
</head>
<body>
  <section class="card card--front" aria-label="Business card front">
    <div class="front__header"></div>
    <div class="brand-name">Breezeway<br>Climate</div>
    <div class="person">
      <div class="person__name">Dominic Vasquerelli</div>
      <div class="person__title">President</div>
    </div>
    <div class="contact">
      <div class="contact__icons">
        <svg class="contact__icon" viewBox="0 0 22 22" aria-hidden="true">
          <circle cx="11" cy="11" r="11" fill="#f3d47c"/>
          <path d="M7 6.5c.6-.6 1.4-.5 1.8.1l1 1.6c.3.5.2 1-.2 1.4l-.6.6c.6 1.2 1.6 2.2 2.8 2.8l.6-.6c.4-.4.9-.5 1.4-.2l1.6 1c.6.4.7 1.2.1 1.8l-.7.7c-1 1-4 .2-6.2-2s-3-5.2-2-6.2z" fill="#a32033"/>
        </svg>
        <svg class="contact__icon" viewBox="0 0 22 22" aria-hidden="true">
          <circle cx="11" cy="11" r="11" fill="#f3d47c"/>
          <rect x="5.5" y="7.5" width="11" height="7.5" rx="1" fill="#a32033"/>
          <path d="M5.8 8l5.2 4 5.2-4" fill="none" stroke="#f3d47c" stroke-width="1"/>
        </svg>
        <svg class="contact__icon" viewBox="0 0 22 22" aria-hidden="true">
          <circle cx="11" cy="11" r="11" fill="#f3d47c"/>
          <circle cx="11" cy="11" r="5.5" fill="none" stroke="#a32033" stroke-width="1.4"/>
          <path d="M5.5 11h11M11 5.5c-2.5 3-2.5 8 0 11M11 5.5c2.5 3 2.5 8 0 11" fill="none" stroke="#a32033" stroke-width="1.1"/>
        </svg>
      </div>
      <div>555-214-6837</div>
      <div>info@breezewayclimate.example</div>
      <div>www.BreezewayClimateLLC.example</div>
    </div>
  </section>

  <section class="card card--back" aria-label="Business card back">
    <div class="brand-name">Breezeway<br>Climate</div>
  </section>
</body>
</html>
```